New Packaging Design Project

Wine packaging redesign. Retail partner requested a redesign of a private label wine. The old label is attached. Our partner liked the Lantern and Briar label and wanted something similar. There will be a logo added to the top of the label

Went on vacation/holiday

```html
<!DOCTYPE html>
<html lang="en">
<head>
<meta charset="utf-8">
<title>Napa Valley Red Blend – Wine Label</title>
<link rel="stylesheet" href="https://fonts.googleapis.com/css2?family=Cormorant+Garamond:wght@400;500&family=Roboto:wght@500&family=Roboto+Condensed:wght@400&display=swap">
<style>
  :root {
    --page-bg: #ffffff;
    --label-bg: #7b7667;
    --label-bg-light: #827d6e;
    --title-gold: #e9cf84;
    --subtitle-white: #f4f1ea;
    --varietal-beige: #d3c3a8;
    --scene-sky: #7d7869;
    --scene-hills: #5f5d51;
    --scene-ground: #6c6a5d;
  }
  * { margin: 0; padding: 0; box-sizing: border-box; }
  html, body {
    width: 720px;
    height: 1200px;
    overflow: hidden;
    background: var(--page-bg);
  }
  .canvas {
    position: relative;
    width: 720px;
    height: 1200px;
  }
  .wine-label {
    position: absolute;
    left: 60px;
    top: 150px;
    width: 600px;
    height: 900px;
    background: linear-gradient(180deg, var(--label-bg) 0%, var(--label-bg) 78%, var(--label-bg-light) 100%);
    text-align: center;
  }
  .region-title {
    position: absolute;
    top: 226px;
    left: 0;
    width: 100%;
    font-family: "Cormorant Garamond", serif;
    font-weight: 500;
    font-size: 66px;
    letter-spacing: 1px;
    color: var(--title-gold);
    line-height: 1;
  }
  .wine-style {
    position: absolute;
    top: 362px;
    left: 0;
    width: 100%;
    font-family: "Roboto", sans-serif;
    font-weight: 500;
    font-size: 28px;
    letter-spacing: 5px;
    color: var(--subtitle-white);
    line-height: 1;
  }
  .landscape-art {
    position: absolute;
    top: 440px;
    left: 0;
    width: 600px;
    height: 275px;
    display: block;
  }
  .varietals {
    position: absolute;
    top: 786px;
    left: 0;
    width: 100%;
    font-family: "Roboto Condensed", sans-serif;
    font-size: 21px;
    letter-spacing: 1.5px;
    color: var(--varietal-beige);
    line-height: 32px;
  }
  .varietals .divider { padding: 0 4px; }
  .vintage {
    position: absolute;
    top: 846px;
    left: 0;
    width: 100%;
    font-family: "Cormorant Garamond", serif;
    font-size: 24px;
    letter-spacing: 2px;
    color: var(--subtitle-white);
    line-height: 1;
  }
</style>
</head>
<body>
  <main class="canvas">
    <section class="wine-label">
      <h1 class="region-title">NAPA VALLEY</h1>
      <h2 class="wine-style">RED BLEND</h2>

      <svg class="landscape-art" viewBox="0 0 600 275" role="img" aria-label="Illustration of a misty valley with rolling hills, a rising sun and trees">
        <defs>
          <linearGradient id="valley-tones" x1="0" y1="0" x2="0" y2="1">
            <stop offset="0" stop-color="var(--scene-sky)"/>
            <stop offset="0.45" stop-color="var(--scene-hills)"/>
            <stop offset="1" stop-color="var(--scene-ground)"/>
          </linearGradient>
        </defs>
        <rect width="600" height="275" fill="url(#valley-tones)"/>
      </svg>

      <p class="varietals">
        MERLOT<span class="divider">|</span>CABERNET SAUVIGNON<br>
        CABERNET FRANC<span class="divider">|</span>PETIT VERDOT<span class="divider">|</span>MALBEC
      </p>
      <p class="vintage">2018</p>
    </section>
  </main>
</body>
</html>
```